Quillmark Hall Business Card

I need a business card design. We are a collaborate online training company. Our colors are gray and green. Our website is QuillmarkHall.com

I would like an area for a profile picture within the card

```html
<!DOCTYPE html>
<html lang="en">
<head>
<meta charset="utf-8">
<title>Quillmark Hall Business Card</title>
<link rel="stylesheet" href="https://fonts.googleapis.com/css2?family=Open+Sans:wght@400;600;700;800&display=swap">
<style>
  :root {
    --stage: #2b2b2b;
    --ink: #111111;
    --card-black: #050505;
    --card-white: #ffffff;
    --green: #7dc242;
    --text: #1a1a1a;
    --photo: #c9cfc4;
  }
  * { box-sizing: border-box; margin: 0; padding: 0; }
  html, body { width: 1200px; height: 900px; overflow: hidden; }
  body {
    background: var(--stage);
    font-family: "Open Sans", Arial, sans-serif;
    position: relative;
  }
  .card {
    position: absolute;
    left: 260px;
    width: 680px;
    height: 388px;
    overflow: hidden;
    box-shadow: 0 10px 30px rgba(0,0,0,0.45);
  }
  .card--back { top: 40px; background: var(--card-black); }
  .card--front { top: 468px; background: var(--card-white); }

  .brand {
    position: absolute;
    display: flex;
    align-items: center;
    gap: 10px;
    white-space: nowrap;
  }
  .brand__dot {
    border-radius: 50%;
    background: var(--green);
    flex: none;
  }
  .brand__name {
    font-weight: 800;
    letter-spacing: -1px;
    line-height: 1;
  }
  .card--back .brand { right: 48px; top: 160px; }
  .card--back .brand__dot { width: 44px; height: 44px; }
  .card--back .brand__name { color: #ffffff; font-size: 40px; }
  .back-url {
    position: absolute;
    right: 50px; top: 212px;
    color: var(--green);
    font-size: 17px;
    font-weight: 600;
  }

  .card--front .brand { left: 36px; top: 178px; }
  .card--front .brand__dot { width: 38px; height: 38px; }
  .card--front .brand__name { color: var(--ink); font-size: 31px; }

  .profile-photo {
    position: absolute;
    left: 36px; top: 56px;
    width: 96px; height: 96px;
    border-radius: 50%;
    background: radial-gradient(circle at 50% 40%, #dde2d8, var(--photo));
    border: 3px solid var(--green);
  }

  .divider {
    position: absolute;
    left: 352px; top: 56px;
    width: 2px; height: 190px;
    background: var(--green);
  }
  .contact {
    position: absolute;
    left: 378px; top: 54px;
    color: var(--text);
    font-size: 15px;
    line-height: 1.4;
  }
  .contact__name { font-size: 21px; font-weight: 800; line-height: 1.1; }
  .contact__name span { color: var(--green); }
  .contact__role { font-size: 14px; margin-bottom: 14px; }
  .contact__address { margin-bottom: 10px; }
  .contact__line { display: flex; align-items: center; gap: 7px; }
  .contact__icon { width: 16px; height: 16px; flex: none; }

  .front-bands { position: absolute; left: 0; top: 0; }
</style>
</head>
<body>

<section class="card card--back" aria-label="Card back">
  <div class="brand">
    <span class="brand__dot"></span>
    <span class="brand__name">Quillmark Hall</span>
  </div>
  <div class="back-url">www.quillmarkhall.com</div>
</section>

<section class="card card--front" aria-label="Card front">
  <svg class="front-bands" width="680" height="388" viewBox="0 0 680 388" aria-hidden="true">
    <polygon points="0,360 500,360 520,334 680,334 680,388 0,388" fill="#050505"/>
    <polygon points="520,334 548,300 680,272 680,334" fill="#7dc242"/>
  </svg>

  <div class="profile-photo" role="img" aria-label="Profile photo of the founder"></div>

  <div class="brand">
    <span class="brand__dot"></span>
    <span class="brand__name">Quillmark Hall</span>
  </div>

  <div class="divider"></div>

  <div class="contact">
    <div class="contact__name">Dana <span>Whitfield</span></div>
    <div class="contact__role">Founder</div>
    <div class="contact__address">418 N Alder Ave. Suite 7<br>Fairmont, Oregon 97402</div>
    <div class="contact__line">
      <svg class="contact__icon" viewBox="0 0 16 16" aria-hidden="true"><circle cx="8" cy="8" r="8" fill="#111"/><path d="M5 4.5l1.6-.4.9 2-1 .8c.5 1.1 1.3 1.9 2.4 2.4l.8-1 2 .9-.4 1.6c-3.4.2-6.5-2.9-6.3-6.3z" fill="#7dc242"/></svg>
      <span>(555) 204-6391</span>
    </div>
    <div class="contact__line">
      <svg class="contact__icon" viewBox="0 0 16 16" aria-hidden="true"><circle cx="8" cy="8" r="8" fill="#111"/><rect x="4" y="5" width="8" height="6" fill="#7dc242"/><path d="M4 5l4 3.5L12 5" fill="none" stroke="#111" stroke-width="0.9"/></svg>
      <span>info@quillmarkhall.com</span>
    </div>
    <div class="contact__line">
      <svg class="contact__icon" viewBox="0 0 16 16" aria-hidden="true"><circle cx="8" cy="8" r="8" fill="#111"/><circle cx="8" cy="8" r="4.5" fill="none" stroke="#7dc242" stroke-width="1"/><path d="M3.5 8h9M8 3.5v9M5.2 5.5h5.6M5.2 10.5h5.6" stroke="#7dc242" stroke-width="0.8"/></svg>
      <span>www.quillmarkhall.com</span>
    </div>
  </div>
</section>

</body>
</html>
```